Australian Software Consultancy needs new Business Card Design

Design Business Card based on existing design artefacts (attached). We are open to all designs. As its a 2 sided design and we thought it might be quite striking to have one side with a black background and te other side with a white background.

Target Market(s)

Financial Services mainly.

Industry/Entity Type

Business

Contact Information for Business Card

Name :
Position :
Email :

Requirements
Must have
• Funky design using our existing assets

```html
<!DOCTYPE html>
<html lang="en">
<head>
<meta charset="utf-8">
<title>Quorvane Business Card</title>
<link rel="stylesheet" href="https://fonts.googleapis.com/css2?family=Montserrat:wght@700&family=Sansita:wght@800&display=swap">
<style>
  :root {
    --stage: #717171;
    --card-light: #ffffff;
    --card-dark: #231f20;
    --brand-red: #ec1c24;
    --ink: #1e1a1b;
  }
  html, body {
    margin: 0;
    padding: 0;
    width: 1200px;
    height: 1200px;
    overflow: hidden;
    background: var(--stage);
  }
  .canvas {
    position: relative;
    width: 1200px;
    height: 1200px;
  }
  .card {
    position: absolute;
    overflow: hidden;
  }
  .card--front {
    left: 184px; top: 61px; width: 833px; height: 476px;
    background: var(--card-light);
  }
  .card--back {
    left: 181px; top: 632px; width: 840px; height: 480px;
    background: var(--card-dark);
  }
  .card__texture {
    position: absolute;
    inset: 0;
  }
  .card--front .card__texture {
    background: linear-gradient(135deg, #ffffff 0%, #f6f6f6 45%, #ffffff 70%, #f7f7f7 100%);
  }
  .card--back .card__texture {
    background: radial-gradient(ellipse at 50% 50%, #3a3536 0%, #2a2627 45%, var(--card-dark) 100%);
  }
  .brand-ring {
    position: absolute;
    border-radius: 50%;
    border: 10px solid var(--brand-red);
    box-sizing: border-box;
  }
  .card--front .brand-ring {
    left: 121px; top: 63px; width: 210px; height: 210px;
  }
  .card--back .brand-ring {
    left: 335px; top: 78px; width: 168px; height: 168px;
  }
  .brand-name {
    position: absolute;
    font-family: "Montserrat", sans-serif;
    font-weight: 700;
    letter-spacing: 1px;
    white-space: nowrap;
    text-align: center;
    line-height: 1;
  }
  .card--front .brand-name {
    left: 44px; top: 340px; width: 362px;
    font-size: 52px;
    color: var(--ink);
  }
  .card--back .brand-name {
    left: 0; top: 298px; width: 840px;
    font-size: 74px;
    color: #ffffff;
  }
  .person-name {
    position: absolute;
    left: 455px; top: 126px; width: 360px;
    text-align: center;
    font-family: "Sansita", sans-serif;
    font-weight: 800;
    font-size: 48px;
    letter-spacing: 1px;
    color: var(--ink);
    margin: 0;
    line-height: 1;
  }
  .person-role {
    position: absolute;
    left: 455px; top: 214px; width: 360px;
    text-align: center;
    font-family: "Sansita", sans-serif;
    font-weight: 800;
    font-size: 16px;
    letter-spacing: 0.5px;
    color: var(--brand-red);
    margin: 0;
    line-height: 1;
  }
  .contact {
    position: absolute;
    left: 460px; top: 359px;
    display: flex;
    align-items: center;
    gap: 8px;
  }
  .contact__icon {
    width: 48px; height: 31px;
  }
  .contact__web {
    font-family: "Sansita", sans-serif;
    font-weight: 800;
    font-size: 25px;
    color: var(--brand-red);
    letter-spacing: 0.5px;
  }
  .contact__web-domain { color: var(--ink); }
</style>
</head>
<body>
<main class="canvas">
  <section class="card card--front">
    <div class="card__texture" role="img" aria-label="Faint light grey faceted polygon texture"></div>
    <div class="brand-ring"></div>
    <div class="brand-name">QUORVANE</div>
    <h1 class="person-name">Liam Carter</h1>
    <p class="person-role">Software Consultant</p>
    <div class="contact">
      <svg class="contact__icon" viewBox="0 0 48 31" aria-hidden="true">
        <rect x="0" y="0" width="48" height="31" fill="var(--ink)"/>
        <polyline points="1,1 24,18 47,1" fill="none" stroke="#ffffff" stroke-width="2.5"/>
        <line x1="1" y1="30" x2="18" y2="14" stroke="#ffffff" stroke-width="2"/>
        <line x1="47" y1="30" x2="30" y2="14" stroke="#ffffff" stroke-width="2"/>
      </svg>
      <span class="contact__web">www.<span class="contact__web-domain">liamcarter</span>.com</span>
    </div>
  </section>

  <section class="card card--back">
    <div class="card__texture" role="img" aria-label="Dark background with crossing grey rounded circuit lines and white light glints"></div>
    <div class="brand-ring"></div>
    <div class="brand-name">QUORVANE</div>
  </section>
</main>
</body>
</html>
```